Business Card Design

Extremely classy understated design.

Printing in fancy scrip or hand writing.

Conservative color scheme such as black print on beige paper. I am sure you have much better ideas than I would have.

I am involved in a number of different businesses and require a simple elegant business card.

I would like a object on the card, such as, a bald eagle, an antique Ashcombe Vance, a water fall or a beautiful flower.
Updates

My name is: Leon T. Marsh Not Leon T. Marsh Investments Investments is my occupation Most of the designs are not acceptable. Very disappointed with results.

Industry/Entity Type

Business

Contact Information for Business Card

Leon T Marsh
Investments
555 614 2790
kestrellm@postvale.net

```html
<!DOCTYPE html>
<html lang="en">
<head>
<meta charset="utf-8">
<title>Leon T. Marsh – Business Card</title>
<link rel="stylesheet" href="https://fonts.googleapis.com/css2?family=Great+Vibes&family=Source+Sans+3:wght@400&display=swap">
<style>
  :root {
    --teal: #2a7599;
    --card-light: #ffffff;
    --card-edge: #dcdddf;
    --faint-mark: #c6c7c9;
  }
  html, body {
    margin: 0;
    padding: 0;
    width: 1200px;
    height: 702px;
    overflow: hidden;
    background: var(--card-edge);
  }
  .card {
    position: relative;
    width: 1200px;
    height: 702px;
    overflow: hidden;
    background: radial-gradient(ellipse 60% 70% at 48% 48%, var(--card-light) 0%, #eeeeef 55%, var(--card-edge) 100%);
    font-family: "Source Sans 3", "Myriad Pro", sans-serif;
    color: var(--teal);
  }
  .faint-mark {
    position: absolute;
    left: 776px;
    top: 346px;
    width: 420px;
    height: 420px;
    border-radius: 50%;
    background: var(--faint-mark);
    opacity: 0.75;
  }
  .brand {
    position: absolute;
    left: 0;
    top: 92px;
    width: 1200px;
    text-align: center;
  }
  .brand-dot {
    display: block;
    width: 150px;
    height: 150px;
    margin: 0 auto 10px;
    border-radius: 50%;
    background: var(--teal);
  }
  .brand-name {
    font-family: "Great Vibes", cursive;
    font-size: 40px;
    font-weight: 400;
    color: var(--teal);
  }
  .holder {
    position: absolute;
    right: 633px;
    top: 440px;
    margin: 0;
    text-align: right;
    white-space: nowrap;
  }
  .holder-name {
    display: block;
    font-family: "Great Vibes", cursive;
    font-size: 58px;
    font-weight: 400;
    line-height: 1.1;
  }
  .holder-role {
    display: block;
    margin-top: 4px;
    font-size: 24px;
    font-weight: 400;
    letter-spacing: 0.04em;
  }
  .divider {
    position: absolute;
    left: 596px;
    top: 432px;
    width: 4px;
    height: 198px;
    background: var(--teal);
  }
  .contact {
    position: absolute;
    left: 644px;
    margin: 0;
    display: flex;
    align-items: center;
    white-space: nowrap;
  }
  .contact svg { flex: none; }
  .contact-email { top: 472px; font-size: 23px; }
  .contact-email svg { margin-right: 16px; }
  .contact-phone { top: 540px; font-size: 29px; }
  .contact-phone svg { margin-right: 12px; }
</style>
</head>
<body>
<main class="card">
  <div class="faint-mark" aria-hidden="true"></div>

  <div class="brand">
    <span class="brand-dot" aria-hidden="true"></span>
    <span class="brand-name">Leon T Marsh</span>
  </div>

  <h1 class="holder">
    <span class="holder-name">Leon T. Marsh</span>
    <span class="holder-role">Investments</span>
  </h1>

  <div class="divider" aria-hidden="true"></div>

  <p class="contact contact-email">
    <svg width="30" height="30" viewBox="0 0 30 30" aria-hidden="true">
      <g fill="none" stroke="var(--teal)" stroke-width="2.4">
        <circle cx="15" cy="15" r="12"/>
        <ellipse cx="15" cy="15" rx="5" ry="12"/>
        <line x1="3" y1="15" x2="27" y2="15"/>
        <line x1="15" y1="3" x2="15" y2="27"/>
        <line x1="5" y1="9" x2="25" y2="9"/>
        <line x1="5" y1="21" x2="25" y2="21"/>
      </g>
    </svg>
    kestrellm@postvale.net
  </p>

  <p class="contact contact-phone">
    <svg width="38" height="46" viewBox="0 0 38 46" aria-hidden="true">
      <path fill="var(--teal)" d="M9 2c2-1 4 0 5 2l3 7c1 2 0 4-2 5l-3 2c1 5 4 10 8 13l3-2c2-1 4-1 5 1l5 6c1 2 1 4-1 5l-4 3c-3 2-7 1-10-1C9 37 3 27 2 17 1 12 2 7 5 4z"/>
    </svg>
    555 614 2790
  </p>
</main>
</body>
</html>
```